Brelvanhomes42.com needs a website.

I'm looking for a website that offeres education and courses about the QZ home loan. This will teach people what they need to know about using the QZ loan. I need a website design that will allow the use of video, have sections to educate about the myths out there, use blue and red which are patriotic colors.

```html
<!DOCTYPE html>
<html lang="en">
<head>
<meta charset="utf-8">
<title>QZ Mortgage – QZ Home Loan Education</title>
<link href="https://fonts.googleapis.com/css2?family=Lato:ital,wght@0,400;0,700;0,900;1,400&display=swap" rel="stylesheet">
<style>
:root{
  --blue:#1a5fc4;
  --red:#e0100f;
  --dark:#262626;
  --darker:#1c1c1c;
  --light:#f3f3f3;
  --text:#333;
  --muted:#555;
  --white:#fff;
}
*{box-sizing:border-box;margin:0;padding:0}
html,body{width:1200px;height:4955px;overflow:hidden}
body{font-family:'Lato',sans-serif;color:var(--text);background:var(--white);position:relative}
a{color:inherit;text-decoration:none}
.abs{position:absolute}
.btn{display:inline-block;background:var(--red);color:var(--white);font-weight:700;font-size:17px;padding:0 30px;height:50px;line-height:50px;text-transform:uppercase}
.section-title{position:absolute;left:0;width:1200px;text-align:center;font-size:29px;font-weight:900;color:var(--dark);text-transform:uppercase}
.section-title span{color:var(--blue)}
.photo{position:absolute}

/* top bar */
.topbar{top:0;left:0;width:1200px;height:58px;background:var(--blue);color:var(--white)}
.social{display:flex;gap:16px;align-items:center}
.social i{display:block;width:18px;height:18px;border-radius:50%;background:var(--white)}
.topbar .social{position:absolute;left:72px;top:20px}
.topbar .contact{position:absolute;right:72px;top:18px;display:flex;gap:34px;font-size:17px;align-items:center}
.topbar .contact span{display:flex;gap:10px;align-items:center}

/* nav */
.nav{top:58px;left:0;width:1200px;height:90px;background:var(--white)}
.logo{position:absolute;left:74px;top:26px;font-size:29px;font-weight:900;color:var(--blue)}
.menu{position:absolute;right:74px;top:36px;display:flex;gap:31px;font-size:15px;font-weight:700;color:var(--dark)}
.menu .active{color:var(--red)}

/* hero */
.hero{top:148px;left:0;width:1200px;height:702px}
.hero .photo{inset:0;background:linear-gradient(100deg,#8a6b55 0%,#4b4846 30%,#b9a898 55%,#6a5a50 80%,#a4978c 100%)}
.hero-text{position:absolute;left:0;width:1200px;top:238px;text-align:center;color:var(--white);text-transform:uppercase;font-weight:700}
.hero-text .small{font-size:50px;line-height:56px}
.hero-text .big{font-size:74px;line-height:84px;font-weight:900}
.hero .btn{position:absolute;left:492px;top:410px;width:216px;padding:0;text-align:center}
.dots{position:absolute;left:547px;top:648px;display:flex;gap:13px}
.dots i{width:16px;height:16px;border-radius:50%;border:2px solid var(--white)}
.dots i.on{background:var(--white)}

/* welcome */
.welcome{top:850px;left:0;width:1200px;height:481px;background:var(--light)}
.intro{position:absolute;width:500px;text-align:center}
.intro h2{font-size:29px;font-weight:900;text-transform:uppercase;color:var(--dark);margin-bottom:12px}
.intro h2 span{color:var(--blue)}
.intro p{font-size:16px;line-height:28px;color:var(--muted);margin-bottom:26px}
.welcome .intro{left:72px;top:148px}
.welcome-art{top:904px;left:600px}

/* courses */
.courses-title{top:1474px}
.card{position:absolute;top:1542px;width:331px;height:414px;background:var(--light);text-align:center}
.card .photo{position:relative;height:208px}
.card h3{font-size:18px;font-weight:900;color:var(--blue);margin:22px 0 10px;text-transform:uppercase}
.card p{font-size:15.5px;line-height:26px;color:var(--muted);padding:0 24px;margin-bottom:24px}
.card .btn{height:50px;line-height:50px;font-size:16px}
.play{position:absolute;left:50%;top:50%;margin:-20px 0 0 -20px}
.arrow{position:absolute;top:1738px}

/* education */
.education{top:2102px;left:0;width:1200px;height:481px;background:var(--light)}
.education .intro{left:600px;top:88px;width:510px}
.education-art{top:2042px;left:0}

/* news */
.news-title{top:2653px}
.news-main{position:absolute;left:75px;top:2729px;width:512px}
.news-main .photo{position:relative;height:252px;background:linear-gradient(135deg,#d9dde2,#b9bec5 60%,#8b8f96)}
.news-main h3{font-size:23px;font-weight:700;color:var(--blue);margin:28px 0 8px}
.news-main p{font-size:14px;line-height:23px;color:var(--muted)}
.read{display:block;color:var(--red);font-weight:700;font-size:16px;margin-top:10px}
.news-item{position:absolute;left:615px;width:520px;height:120px}
.news-item .photo{left:0;top:0;width:150px;height:120px}
.news-item .txt{position:absolute;left:179px;top:4px;width:330px}
.news-item h4{font-size:22px;font-weight:700;color:var(--blue);margin-bottom:6px}
.news-item p{font-size:13.5px;line-height:23px;color:var(--muted)}
.news-item .read{margin-top:6px}

/* testimonials */
.testimonials{top:3219px;left:0;width:1200px;height:469px;background:linear-gradient(110deg,#1d57c0 0%,#7a2f7a 50%,#e10f10 100%);color:var(--white);text-align:center}
.testimonials h2{position:absolute;left:0;width:1200px;top:60px;font-size:29px;font-weight:900}
.quote{position:absolute;left:140px;width:920px;top:118px;font-size:18px;line-height:29px;font-style:italic}
.avatar{position:absolute;left:548px;top:240px;width:92px;height:92px;border-radius:50%;background:linear-gradient(160deg,#f5b632,#e69a1f)}
.quote-mark{position:absolute;left:622px;top:284px}
.who{position:absolute;left:0;width:1200px;top:350px;font-size:16px;font-weight:700}
.who small{display:block;font-weight:400;font-size:14px;margin-top:4px}
.t-arrow{position:absolute;top:206px}

/* blog */
.blog-title{top:3745px}
.post{position:absolute;top:3811px;width:331px;text-align:center}
.post .photo{position:relative;height:202px}
.post h3{font-size:19px;font-weight:900;line-height:27px;color:var(--blue);margin:36px 0 10px;text-transform:uppercase}
.post p{font-size:14.5px;line-height:24px;color:var(--muted);padding:0 30px;margin-bottom:34px}

/* features */
.footer-band{top:4508px;left:0;width:1200px;height:372px;background:var(--dark)}
.feature{position:absolute;top:4394px;width:346px;height:225px;color:var(--white);text-align:center}
.feature.blue{background:var(--blue)}
.feature.red{background:var(--red)}
.feature .badge{position:absolute;left:118px;top:-52px;width:110px;height:110px;border-radius:50%;border:5px solid var(--white);display:flex;align-items:center;justify-content:center}
.feature h3{position:absolute;left:0;width:100%;top:90px;font-size:27px;line-height:30px;font-weight:900;text-transform:uppercase}
.feature .ghost{position:absolute;left:50%;transform:translateX(-50%);top:162px;border:2px solid var(--white);padding:0 14px;height:34px;line-height:30px;font-size:14px;font-weight:700;text-transform:uppercase}

/* footer */
.foot-logo{left:75px;top:4722px;font-size:29px;font-weight:900;color:var(--white)}
.foot-col{position:absolute;top:4665px;color:var(--white)}
.foot-col h4{font-size:16px;font-weight:700;margin-bottom:14px;text-transform:uppercase}
.links{display:grid;grid-template-columns:100px 100px;row-gap:12px;font-size:14px;color:#ddd}
.info li{list-style:none;display:flex;gap:18px;font-size:14px;line-height:26px;color:#ddd;margin-bottom:6px}
.info svg{flex:none;margin-top:6px}
.field{width:242px;height:40px;background:var(--white);color:#666;font-size:13px;padding:12px 14px;margin-bottom:12px}
.signup{margin-left:154px;background:var(--red);height:40px;line-height:40px;padding:0 14px;font-size:14px;font-weight:700;display:inline-block}
.copybar{top:4880px;left:0;width:1200px;height:75px;background:var(--darker);color:#ccc}
.copybar .copy{position:absolute;left:75px;top:30px;font-size:12px}
.copybar .social{position:absolute;right:90px;top:28px}
.copybar .social i{background:#ddd}
</style>
</head>
<body>

<header class="topbar abs">
  <div class="social" aria-label="Social links"><i></i><i></i><i></i><i></i><i></i><i></i></div>
  <div class="contact">
    <span><svg width="16" height="16" viewBox="0 0 24 24"><path fill="#fff" d="M6.6 10.8a15 15 0 0 0 6.6 6.6l2.2-2.2c.3-.3.7-.4 1-.2 1.1.4 2.3.6 3.6.6.6 0 1 .4 1 1V20c0 .6-.4 1-1 1A17 17 0 0 1 3 4c0-.6.4-1 1-1h3.5c.6 0 1 .4 1 1 0 1.3.2 2.5.6 3.6.1.3 0 .7-.2 1z"/></svg>+1-555-014-4242</span>
    <span><svg width="16" height="13" viewBox="0 0 24 18"><path fill="#fff" d="M0 0h24v18H0z"/><path fill="none" stroke="#1a5fc4" stroke-width="2" d="M1 1l11 9 11-9"/></svg>info@brelvanhomes42.com</span>
  </div>
</header>

<nav class="nav abs">
  <div class="logo">QZ MORTGAGE</div>
  <div class="menu">
    <a class="active">HOME</a><a>ABOUT US</a><a>SERVICES</a><a>COURSES</a><a>BLOG</a><a>CAREER</a><a>CONTACT US</a>
  </div>
</nav>

<section class="hero abs">
  <div class="photo" role="img" aria-label="Loan advisor explaining a home loan to a couple at a laptop"></div>
  <div class="hero-text">
    <div class="small">Welcome to</div>
    <div class="big">QZ Mortgage</div>
  </div>
  <a class="btn">Book your course</a>
  <div class="dots"><i class="on"></i><i></i><i></i><i></i></div>
</section>

<section class="welcome abs">
  <div class="intro">
    <h2>Welcome to <span>QZ Mortgage</span></h2>
    <p>Nunc sollicitudin congue lacus ut vestibulumdonec at varius augue. Sed efficitur venenatis tellus, non dictum quam venenatis sit amet. Nulla turpis mi, vulputate et diam quis, pharetra posuere justo placerat dolor a risus euismod, sed tempor elit porta.</p>
    <a class="btn">Read more</a>
  </div>
</section>
<svg class="welcome-art abs" width="590" height="484" viewBox="0 0 590 484" role="img" aria-label="Hand touching a digital house icon above a laptop">
  <defs><linearGradient id="g1" x1="0" y1="0" x2="1" y2="1"><stop offset="0" stop-color="#3c5a6a"/><stop offset=".5" stop-color="#8fa3ad"/><stop offset="1" stop-color="#2f3a40"/></linearGradient></defs>
  <polygon points="95,0 588,0 588,0 500,484 0,484" fill="none"/>
  <polygon points="95,0 588,0 540,470 0,470" fill="var(--red)"/>
  <polygon points="112,16 590,16 590,484 20,484" fill="url(#g1)"/>
</svg>

<h2 class="section-title courses-title">Courses <span>offer</span></h2>
<svg class="arrow" style="left:34px" width="22" height="22" viewBox="0 0 22 22"><path d="M20 11H3M10 3l-8 8 8 8" fill="none" stroke="var(--blue)" stroke-width="3"/></svg>
<svg class="arrow" style="left:1140px" width="22" height="22" viewBox="0 0 22 22"><path d="M2 11h17M12 3l8 8-8 8" fill="none" stroke="var(--blue)" stroke-width="3"/></svg>

<article class="card" style="left:75px">
  <div class="photo" role="img" aria-label="Video: couple reviewing loan papers with a laptop" style="background:linear-gradient(135deg,#e7e2da,#b9a792 60%,#7d6c5c)">
    <svg class="play" width="40" height="40" viewBox="0 0 40 40"><circle cx="20" cy="20" r="18" fill="none" stroke="#fff" stroke-width="3"/><path d="M16 12l12 8-12 8z" fill="#fff"/></svg>
  </div>
  <h3>Course heading</h3>
  <p>Nunc sollicitudin congue lacus ut ve stibulumdonec at varius augue enim ipsam voluptatem quia</p>
  <a class="btn">Read more</a>
</article>
<article class="card" style="left:435px">
  <div class="photo" role="img" aria-label="Video: woman reading a loan document" style="background:linear-gradient(135deg,#efe7dc,#d0b49b 55%,#9a7f68)">
    <svg class="play" width="40" height="40" viewBox="0 0 40 40"><circle cx="20" cy="20" r="18" fill="none" stroke="#fff" stroke-width="3"/><path d="M16 12l12 8-12 8z" fill="#fff"/></svg>
  </div>
  <h3>Course heading</h3>
  <p>Nunc sollicitudin congue lacus ut ve stibulumdonec at varius augue enim ipsam voluptatem quia</p>
  <a class="btn">Read more</a>
</article>
<article class="card" style="left:796px">
  <div class="photo" role="img" aria-label="Video: advisors meeting with a client at a desk" style="background:linear-gradient(135deg,#ece6dd,#b39a84 55%,#5e4d40)">
    <svg class="play" width="40" height="40" viewBox="0 0 40 40"><circle cx="20" cy="20" r="18" fill="none" stroke="#fff" stroke-width="3"/><path d="M16 12l12 8-12 8z" fill="#fff"/></svg>
  </div>
  <h3>Course heading</h3>
  <p>Nunc sollicitudin congue lacus ut ve stibulumdonec at varius augue enim ipsam voluptatem quia</p>
  <a class="btn">Read more</a>
</article>

<section class="education abs">
  <div class="intro">
    <h2>Education <span>about myths</span></h2>
    <p>Nunc sollicitudin congue lacus ut vestibulumdonec at varius augue. Sed efficitur venenatis tellus, non dictum quam venenatis sit amet. Nulla turpis mi, vulputate et diam quis, pharetra posuere justo placerat dolor a risus euismod, sed tempor elit porta.</p>
    <a class="btn">Read more</a>
  </div>
</section>
<svg class="education-art abs" width="600" height="484" viewBox="0 0 600 484" role="img" aria-label="Person typing on a laptop showing a mortgage page, pencil cup on desk">
  <defs><linearGradient id="g2" x1="0" y1="0" x2="1" y2="1"><stop offset="0" stop-color="#5a4636"/><stop offset=".5" stop-color="#a48a70"/><stop offset="1" stop-color="#2c3340"/></linearGradient></defs>
  <polygon points="0,16 600,16 520,484 0,484" fill="var(--red)"/>
  <polygon points="0,0 582,0 504,470 0,470" fill="url(#g2)"/>
</svg>

<h2 class="section-title news-title">Latest <span>news</span></h2>
<article class="news-main">
  <div class="photo" role="img" aria-label="Small model house beside a laptop and glasses"></div>
  <h3>Nemo enim ipsam voluptatem quia voluptas</h3>
  <p>Sed ut perspiciatis unde omnis iste natus error sit voluptatem accusantium doloremque explicabo exercitation ullamco laboris nisi ut aliquip ex ea commodo accusantium doloremque.</p>
  <a class="read">Read More</a>
</article>
<article class="news-item" style="top:2729px">
  <div class="photo" role="img" aria-label="Row of small model houses" style="background:linear-gradient(135deg,#5b6570,#c9ccd0 60%,#8d6f5a)"></div>
  <div class="txt"><h4>Nemo enim ipsam.</h4><p>Sed ut perspiciatis unde omnis iste natus error sit voluptatem accusantium dolor</p><a class="read">Read More</a></div>
</article>
<article class="news-item" style="top:2873px">
  <div class="photo" role="img" aria-label="Model house on financial charts" style="background:linear-gradient(135deg,#e9e3da,#c2a486 55%,#7f6450)"></div>
  <div class="txt"><h4>Nemo enim ipsam.</h4><p>Sed ut perspiciatis unde omnis iste natus error sit voluptatem accusantium dolor</p><a class="read">Read More</a></div>
</article>
<article class="news-item" style="top:3014px">
  <div class="photo" role="img" aria-label="Advisor meeting with a couple at a laptop" style="background:linear-gradient(135deg,#cfc8bf,#7b6a5d 55%,#3a3634)"></div>
  <div class="txt"><h4>Nemo enim ipsam.</h4><p>Sed ut perspiciatis unde omnis iste natus error sit voluptatem accusantium dolor</p><a class="read">Read More</a></div>
</article>

<section class="testimonials abs">
  <h2>TESTIMONIALS</h2>
  <svg class="t-arrow" style="left:60px" width="18" height="30" viewBox="0 0 18 30"><path d="M15 2L3 15l12 13" fill="none" stroke="#fff" stroke-width="2.5"/></svg>
  <svg class="t-arrow" style="left:1124px" width="18" height="30" viewBox="0 0 18 30"><path d="M3 2l12 13L3 28" fill="none" stroke="#fff" stroke-width="2.5"/></svg>
  <p class="quote">“Sed ut perspiciatis unde omnis iste natus error sit voluptatem accusantium doloremque laudantium, totam rem aperiam, eaque ipsa quae ab illo inventore veritatis et quasi architecto beatae vitae dicta sunt explicabo. Nemo enim ipsam voluptatem quia voluptas sit aspernatur aut odit aut fugit, sed quia consequuntur magni dolores eos qui ratione voluptatem sequi nesciunt...”</p>
  <div class="avatar" role="img" aria-label="Client portrait"></div>
  <svg class="quote-mark" width="50" height="42" viewBox="0 0 50 42"><rect width="50" height="42" rx="10" fill="var(--red)"/><path d="M10 10h12v12l-6 12h-5l5-12h-6zM28 10h12v12l-6 12h-5l5-12h-6z" fill="#fff"/></svg>
  <div class="who">TOMAS VELDER<small>Location</small></div>
</section>

<h2 class="section-title blog-title">Blog <span>articles</span></h2>
<article class="post" style="left:75px">
  <div class="photo" role="img" aria-label="Older couple reading loan paperwork" style="background:linear-gradient(135deg,#eae6e0,#bfb2a4 55%,#8b7968)"></div>
  <h3>Neque porro quisquam<br>est qui dolorem</h3>
  <p>Nunc sollicitudin congue lacus ut vestibulumdonec at variu non dictum quam venenatis sit amet.</p>
  <a class="btn">Read more</a>
</article>
<article class="post" style="left:435px">
  <div class="photo" role="img" aria-label="Digital house icon over a laptop keyboard" style="background:linear-gradient(135deg,#3a3a3c,#8a8c90 55%,#2a2a2c)"></div>
  <h3>Neque porro quisquam<br>est qui dolorem</h3>
  <p>Nunc sollicitudin congue lacus ut vestibulumdonec at variu non dictum quam venenatis sit amet.</p>
  <a class="btn">Read more</a>
</article>
<article class="post" style="left:796px">
  <div class="photo" role="img" aria-label="Couple reviewing bills at home" style="background:linear-gradient(135deg,#5a4a3e,#a88a70 55%,#3d332c)"></div>
  <h3>Neque porro quisquam<br>est qui dolorem</h3>
  <p>Nunc sollicitudin congue lacus ut vestibulumdonec at variu non dictum quam venenatis sit amet.</p>
  <a class="btn">Read more</a>
</article>

<footer>
  <div class="footer-band abs"></div>

  <div class="feature blue" style="left:75px">
    <div class="badge blue" style="background:var(--blue)"><svg width="34" height="42" viewBox="0 0 34 42"><path d="M0 0h24l10 10v32H0z" fill="#fff"/><path d="M7 18h20M7 25h20M7 32h20" stroke="var(--blue)" stroke-width="3"/></svg></div>
    <h3>Our<br>services</h3>
    <a class="ghost">View services</a>
  </div>
  <div class="feature red" style="left:421px">
    <div class="badge" style="background:var(--red)"><svg width="48" height="40" viewBox="0 0 48 40"><circle cx="24" cy="9" r="7" fill="#fff"/><path d="M12 36c0-10 5-16 12-16s12 6 12 16z" fill="#fff"/><circle cx="9" cy="15" r="5" fill="#fff"/><circle cx="39" cy="15" r="5" fill="#fff"/><path d="M0 34c0-7 4-12 9-12 2 0 3 1 4 2-2 3-3 6-3 10zM48 34c0-7-4-12-9-12-2 0-3 1-4 2 2 3 3 6 3 10z" fill="#fff"/></svg></div>
    <h3>Expert<br>team</h3>
    <a class="ghost">View team</a>
  </div>
  <div class="feature blue" style="left:767px">
    <div class="badge" style="background:var(--blue)"><svg width="46" height="40" viewBox="0 0 46 40"><rect x="2" y="2" width="42" height="28" rx="2" fill="none" stroke="#fff" stroke-width="4"/><path d="M16 38h14M23 30v8" stroke="#fff" stroke-width="4"/></svg></div>
    <h3>Book your<br>favourite course</h3>
    <a class="ghost">Book now</a>
  </div>

  <div class="foot-logo abs">QZ MORTGAGE</div>

  <div class="foot-col" style="left:380px">
    <h4>Site map</h4>
    <div class="links"><a>Home</a><a>Blog</a><a>About Us</a><a>Career</a><a>Services</a><a>Contact Us</a><a>Courses</a></div>
  </div>
  <div class="foot-col" style="left:622px;width:230px">
    <h4>Contact info</h4>
    <ul class="info">
      <li><svg width="12" height="16" viewBox="0 0 12 16"><path d="M6 0a6 6 0 0 1 6 6c0 4-6 10-6 10S0 10 0 6a6 6 0 0 1 6-6z" fill="#fff"/><circle cx="6" cy="6" r="2" fill="var(--dark)"/></svg><span>Nemo enim ipsam volup tatem quia volupta</span></li>
      <li><svg width="14" height="14" viewBox="0 0 24 24"><path fill="#fff" d="M6.6 10.8a15 15 0 0 0 6.6 6.6l2.2-2.2c.3-.3.7-.4 1-.2 1.1.4 2.3.6 3.6.6.6 0 1 .4 1 1V20c0 .6-.4 1-1 1A17 17 0 0 1 3 4c0-.6.4-1 1-1h3.5c.6 0 1 .4 1 1 0 1.3.2 2.5.6 3.6.1.3 0 .7-.2 1z"/></svg><span>1-555-014-4242</span></li>
      <li><svg width="14" height="11" viewBox="0 0 24 18"><path fill="#fff" d="M0 0h24v18H0z"/><path fill="none" stroke="#262626" stroke-width="2" d="M1 1l11 9 11-9"/></svg><span>info@brelvanhomes42.com</span></li>
    </ul>
  </div>
  <div class="foot-col" style="left:884px">
    <h4>Email sign up</h4>
    <div class="field">Enter Name</div>
    <div class="field">Enter Email Address</div>
    <a class="signup">SIGN UP</a>
  </div>

  <div class="copybar abs">
    <div class="copy">Copyright © 2023 QZ Mortgage  All Right Reserved</div>
    <div class="social" aria-label="Social links"><i></i><i></i><i></i><i></i><i></i><i></i></div>
  </div>
</footer>

</body>
</html>
```